Carry The Tide Home

Business Card design

Target Market(s)

People who require support in the commnity

Industry/Entity Type

Mental Health Support

Contact Information for Business Card

Mental Health Support Rosalind Bratten carrythetidehome@mailvane.com.au 0481 637 592 PO Box 629 Kelverton QLD 4571

Colors
6B429C
8869AF
B7A5CE
E3DAEB
F3F0F8

Requirements
Must have
• Logo & details listed above
Should not have
• No red or orange

```html
<!DOCTYPE html>
<html lang="en">
<head>
<meta charset="utf-8">
<title>Carry The Tide Home — Business Card</title>
<link rel="stylesheet" href="https://fonts.googleapis.com/css2?family=Inter:wght@400;700&display=swap">
<style>
  :root {
    --purple: #6b429c;
    --purple-mid: #8869af;
    --lilac: #b7a5ce;
    --mist: #e3daeb;
    --paper: #f4f3f1;
    --ink-grey: #6a6a6a;
    --backdrop: #dcdddf;
  }
  * { box-sizing: border-box; margin: 0; padding: 0; }
  html, body { width: 1200px; height: 1051px; overflow: hidden; }
  body {
    background: var(--backdrop);
    font-family: "Inter", Arial, sans-serif;
    position: relative;
  }
  .card {
    position: absolute;
    left: 280px;
    width: 640px;
    height: 366px;
    background: var(--paper);
    border-bottom: 6px solid var(--purple);
    box-shadow: 0 18px 40px rgba(0,0,0,0.18);
  }
  .card--front { top: 90px; }
  .card--back { top: 596px; }

  .details {
    position: absolute;
    left: 48px;
    top: 62px;
  }
  .details__role,
  .details__name {
    color: var(--purple);
    font-weight: 700;
    font-size: 22px;
    line-height: 1.2;
  }
  .details__address {
    margin-top: 18px;
    color: var(--ink-grey);
    font-size: 16px;
    line-height: 1.4;
  }
  .details__contact {
    margin-top: 18px;
    list-style: none;
    color: var(--ink-grey);
    font-size: 16px;
    line-height: 1.55;
  }
  .details__contact li { display: flex; align-items: center; gap: 8px; }
  .details__contact svg { width: 13px; height: 13px; flex: none; }
  .icon-phone { fill: var(--purple); }
  .icon-mail { fill: none; stroke: var(--purple); stroke-width: 2.4; stroke-linejoin: round; }

  .brand {
    position: absolute;
    display: flex;
    flex-direction: column;
    align-items: center;
    gap: 14px;
  }
  .brand__disc {
    border-radius: 50%;
    background: var(--purple);
  }
  .brand__name {
    color: var(--purple);
    font-weight: 700;
    font-size: 16px;
    letter-spacing: 0.04em;
    white-space: nowrap;
  }
  .card--front .brand { right: 48px; top: 120px; }
  .card--front .brand__disc { width: 150px; height: 150px; }
  .card--back .brand { left: 50%; top: 62px; transform: translateX(-50%); }
  .card--back .brand__disc { width: 170px; height: 170px; }
  .card--back .brand__name { font-size: 18px; }
</style>
</head>
<body>
  <section class="card card--front">
    <div class="details">
      <p class="details__role">Mental Health Support</p>
      <p class="details__name">Rosalind Bratten</p>
      <p class="details__address">PO Box 629<br>Kelverton QLD 4571</p>
      <ul class="details__contact">
        <li>
          <svg class="icon-phone" viewBox="0 0 24 24" aria-hidden="true"><path d="M6.6 10.8a15.1 15.1 0 0 0 6.6 6.6l2.2-2.2a1 1 0 0 1 1-.25 11.4 11.4 0 0 0 3.6.57 1 1 0 0 1 1 1V20a1 1 0 0 1-1 1A17 17 0 0 1 3 4a1 1 0 0 1 1-1h3.5a1 1 0 0 1 1 1c0 1.25.2 2.45.57 3.6a1 1 0 0 1-.25 1z"/></svg>
          0481 637 592
        </li>
        <li>
          <svg class="icon-mail" viewBox="0 0 24 24" aria-hidden="true"><path d="M3 6h18v12H3z M3 6l9 7 9-7"/></svg>
          carrythetidehome@mailvane.com.au
        </li>
      </ul>
    </div>
    <div class="brand">
      <div class="brand__disc"></div>
      <p class="brand__name">Carry The Tide Home</p>
    </div>
  </section>

  <section class="card card--back">
    <div class="brand">
      <div class="brand__disc"></div>
      <p class="brand__name">Carry The Tide Home</p>
    </div>
  </section>
</body>
</html>
```